Slide Master for Harrowfield Engines - A Systematic Hedge Fund

We are looking for someone to produce a theme and slide master for us for our investor presentations. I have uploaded a few examples of templates that we would like to have included:
Main Title
Section Title
Slides with just bullet points
Different image/table configurations with bullet points and foot notes
Biographies of different lengths
A disclaimer (no one will read this but it should still look nice and needs to be in the presentations)
I have also uploaded the company logo, business card and colour definitions. Currently we have a blue colour scheme defined, but it would be nice to get a complementary set of colours so that when we have charts with more elements we can just draw from those.
The most important thing is that the slide master must be of general use to us. We arn't looking to have a specific presentation designed for us, but a theme/style that we can apply ourselves to any presentation we need to give in the future. It should have clearly defined guidelines for where content should go (and if this is different with and without footnotes for example). We would also like it to have a similar feel to the logo/business cards, so matt colours, high contrast, but not busy.
I'm excited to see the results!

```html
<!DOCTYPE html>
<html lang="en">
<head>
<meta charset="utf-8">
<title>Harrowfield Engines – Slide Master</title>
<link rel="stylesheet" href="https://fonts.googleapis.com/css2?family=Montserrat:wght@500;600;700&family=Open+Sans:wght@400;600;700&display=swap">
<style>
  :root {
    --navy: #0b3c74;
    --navy-deep: #08305e;
    --blue: #4a8edb;
    --blue-soft: #6aa5e6;
    --ink: #23364f;
    --text: #4a4f57;
    --paper: #ffffff;
    --stage: #f1f1f2;
    --board: #9d9d9e;
    --track: #e3e5e8;
    --faint: #c4c4c5;
  }
  * { box-sizing: border-box; margin: 0; padding: 0; }
  html, body { width: 1200px; height: 3329px; overflow: hidden; }
  body { position: relative; background: var(--board); font-family: "Open Sans", sans-serif; color: var(--text); }

  .stage { position: absolute; left: 0; top: 0; width: 1200px; height: 805px; background: var(--stage); }
  .hero-slide { position: absolute; left: 220px; top: 190px; transform: scale(1.39); transform-origin: 0 0; }

  .slide { position: absolute; width: 546px; height: 306px; background: var(--paper); overflow: hidden;
           box-shadow: 0 16px 18px -10px rgba(0,0,0,.45); }
  .col-left { left: 48px; } .col-right { left: 615px; }
  .row-1 { top: 864px; } .row-2 { top: 1205px; } .row-3 { top: 1556px; }
  .row-4 { top: 1920px; } .row-5 { top: 2286px; } .row-6 { top: 2642px; }
  .abs { position: absolute; }

  .network-fill { position: absolute; background: linear-gradient(135deg, #f7f8fa 0%, #eceef2 50%, #f8f9fb 100%); }

  .brand { font-family: "Montserrat", sans-serif; font-weight: 700; color: var(--navy); text-align: center; line-height: 1; }
  .brand .l1 { display: block; }
  .brand .l2 { display: block; letter-spacing: .5em; margin-top: 3px; }
  .brand--light { color: #fff; }
  .brand--lg .l1 { font-size: 30px; } .brand--lg .l2 { font-size: 13px; }
  .brand--md .l1 { font-size: 21px; } .brand--md .l2 { font-size: 10px; }
  .brand--sm .l1 { font-size: 11px; } .brand--sm .l2 { font-size: 5.5px; letter-spacing: .45em; margin-top: 1px; }

  .title { font-family: "Montserrat", sans-serif; font-weight: 600; color: #fff; white-space: nowrap; }
  .title .hi { color: var(--blue-soft); }
  .subtitle { font-family: "Open Sans", sans-serif; font-size: 9px; letter-spacing: .22em; color: #fff; text-transform: uppercase; }
  .url { font-family: "Montserrat", sans-serif; font-size: 8.5px; font-weight: 600; letter-spacing: .2em; color: var(--ink); text-transform: uppercase; }
  .url--light { color: #fff; }
  .socials { display: flex; gap: 4px; }
  .socials span { width: 10px; height: 10px; border-radius: 50%; background: #fff; display: block; }
  .socials--dark span { background: var(--ink); }

  .band { position: absolute; left: 0; width: 100%; background: linear-gradient(90deg, var(--navy) 0%, #2766b3 55%, var(--blue) 100%); }

  .slide-rule { position: absolute; left: 16px; top: 6px; width: 2px; height: 30px; background: var(--navy); }
  .slide-heading { position: absolute; left: 28px; top: 16px; font-family: "Montserrat", sans-serif; font-weight: 600; font-size: 19px; color: var(--blue); }
  .slide-brand { position: absolute; right: 20px; top: 16px; }
  .slide-footer { position: absolute; left: 0; bottom: 0; width: 100%; height: 30px; background: var(--navy); display: flex; align-items: center; }
  .slide-footer .globe { width: 7px; height: 7px; border-radius: 50%; border: 1.5px solid #fff; margin-left: 16px; margin-right: 8px; }
  .slide-footer .url { font-family: "Open Sans", sans-serif; font-weight: 400; font-size: 7px; letter-spacing: .18em; text-transform: none; color: #fff; }
  .slide-footer .socials { margin-left: auto; margin-right: 14px; }
  .slide-footer .socials span { width: 12px; height: 12px; }
  .page-no { width: 30px; height: 30px; background: var(--blue); color: #fff; font-family: "Montserrat", sans-serif; font-weight: 700; font-size: 9px; display: flex; align-items: center; justify-content: center; }

  .mini-head { font-family: "Montserrat", sans-serif; font-weight: 700; font-size: 6px; color: var(--ink); text-transform: uppercase; }
  .mini-head--blue { color: var(--blue); }
  .body-tiny { font-size: 6px; line-height: 1.3; color: var(--text); }
  .body-micro { font-size: 4px; line-height: 1.3; color: #7b8088; }

  .photo { position: absolute; }
  .photo--city { background: linear-gradient(160deg, #c9d9ea 0%, #5c7fa6 45%, #20374f 100%); }
  .photo--mono { background: linear-gradient(170deg, #e6e6e6 0%, #5b5b5b 45%, #151515 100%); }
  .photo--office { background: linear-gradient(160deg, #e3dcd4 0%, #a89c90 60%, #6d6258 100%); }
  .photo--glass { background: linear-gradient(150deg, #b9d9ec 0%, #3f86a8 40%, #13303f 100%); }

  .toc-item { position: absolute; display: flex; gap: 10px; width: 230px; }
  .toc-num { font-family: "Montserrat", sans-serif; font-weight: 700; font-size: 32px; color: var(--blue); line-height: 1; width: 46px; }
  .toc-item .mini-head { color: var(--ink); margin-bottom: 2px; }

  .icon-dot { position: absolute; width: 24px; height: 24px; border-radius: 50%; background: var(--navy); border: 2px solid #fff; }
  .icon-dot::after { content: ""; position: absolute; left: 6px; top: 6px; width: 8px; height: 8px; border-radius: 50%; border: 1.5px solid #fff; }

  .bio-caption { position: absolute; height: 13px; background: var(--blue); color: #fff; font-family: "Montserrat", sans-serif; font-size: 6px; font-weight: 600; text-align: center; line-height: 13px; text-transform: uppercase; }

  .feature { position: absolute; width: 100px; text-align: center; }
  .feature .ring { width: 30px; height: 30px; border-radius: 50%; background: var(--navy); margin: 0 auto 5px; box-shadow: 0 0 0 3px #dbe7f6; position: relative; }
  .feature .ring::after { content: ""; position: absolute; left: 9px; top: 9px; width: 12px; height: 12px; border-radius: 50%; border: 2px solid #fff; }

  .watermark { position: absolute; left: 0; top: 3100px; width: 1200px; }
  .watermark .l1 { font-size: 62px; } .watermark .l2 { font-size: 34px; letter-spacing: .7em; margin-top: 14px; padding-left: .7em; }
  .watermark { color: var(--faint); }
</style>
</head>
<body>

<section class="stage" aria-label="Title slide preview">
  <div class="slide hero-slide">
    <div class="network-fill" style="left:0;top:0;width:546px;height:138px" role="img" aria-label="Faint hexagonal network pattern"></div>
    <div class="brand brand--lg abs" style="left:0;width:546px;top:58px"><span class="l1">HARROWFIELD</span><span class="l2">ENGINES</span></div>
    <div class="band" style="top:138px;height:123px">
      <div class="title abs" style="left:0;width:546px;text-align:center;top:24px;font-size:29px"><span class="hi">Master Slide</span> Presentation</div>
      <div class="subtitle abs" style="left:0;width:546px;text-align:center;top:66px">Subtitle goes here</div>
      <div class="socials abs" style="left:255px;top:84px"><span></span><span></span><span></span></div>
    </div>
    <div class="url abs" style="left:0;width:546px;text-align:center;top:278px">www.harrowfieldengines.example</div>
  </div>
</section>

<!-- Title slide: band -->
<div class="slide col-left row-1">
  <div class="network-fill" style="left:0;top:0;width:546px;height:138px" role="img" aria-label="Faint hexagonal network pattern"></div>
  <div class="brand brand--lg abs" style="left:0;width:546px;top:58px"><span class="l1">HARROWFIELD</span><span class="l2">ENGINES</span></div>
  <div class="band" style="top:138px;height:123px">
    <div class="title abs" style="left:0;width:546px;text-align:center;top:24px;font-size:29px"><span class="hi">Master Slide</span> Presentation</div>
    <div class="subtitle abs" style="left:0;width:546px;text-align:center;top:66px">Subtitle goes here</div>
    <div class="socials abs" style="left:255px;top:84px"><span></span><span></span><span></span></div>
  </div>
  <div class="url abs" style="left:0;width:546px;text-align:center;top:278px">www.harrowfieldengines.example</div>
</div>

<!-- Title slide: split -->
<div class="slide col-right row-1">
  <div class="network-fill" style="left:0;top:0;width:272px;height:306px" role="img" aria-label="Faint hexagonal network pattern"></div>
  <div class="brand brand--md abs" style="left:0;width:272px;top:142px"><span class="l1">HARROWFIELD</span><span class="l2">ENGINES</span></div>
  <div class="abs" style="left:272px;top:0;width:274px;height:306px;background:var(--navy)">
    <div class="title abs" style="left:0;width:274px;text-align:center;top:46px;font-size:26px;line-height:1.1"><span class="hi">Master Slide</span><br>PRESENTATION</div>
    <div class="subtitle abs" style="left:0;width:274px;text-align:center;top:116px">Subtitle goes here</div>
    <div class="socials abs" style="left:118px;top:242px"><span></span><span></span><span></span></div>
    <div class="url url--light abs" style="left:0;width:274px;text-align:center;top:274px">www.harrowfieldengines.example</div>
  </div>
</div>

<!-- Title slide: full navy -->
<div class="slide col-left row-2" style="background:var(--navy)">
  <div class="abs" style="left:0;top:190px;width:546px;height:116px;background:linear-gradient(180deg,rgba(255,255,255,0) 0%,rgba(74,142,219,.18) 100%)" role="img" aria-label="Subtle structural line artwork"></div>
  <div class="brand brand--light brand--md abs" style="left:0;width:546px;top:58px"><span class="l1">HARROWFIELD</span><span class="l2">ENGINES</span></div>
  <div class="title abs" style="left:0;width:546px;text-align:center;top:98px;font-size:29px"><span class="hi">Master Slide</span> Presentation</div>
  <div class="subtitle abs" style="left:193px;width:160px;text-align:center;top:140px;border:1px solid #fff;border-radius:10px;padding:3px 0">Subtitle goes here</div>
  <div class="socials abs" style="left:255px;top:256px"><span></span><span></span><span></span></div>
  <div class="url url--light abs" style="left:0;width:546px;text-align:center;top:278px">www.harrowfieldengines.example</div>
</div>

<!-- Disclaimer -->
<div class="slide col-right row-2">
  <div class="slide-rule"></div>
  <div class="slide-heading">Disclaimer</div>
  <div class="brand brand--sm slide-brand"><span class="l1">HARROWFIELD</span><span class="l2">ENGINES</span></div>
  <div class="photo photo--city" style="left:0;top:58px;width:238px;height:198px;border-radius:0 14px 14px 0" role="img" aria-label="Glass office towers seen from below"></div>
  <div class="abs" style="left:224px;top:58px;width:14px;height:198px;background:var(--blue);border-radius:0 14px 14px 0"></div>
  <div class="icon-dot" style="left:221px;top:76px"></div>
  <div class="icon-dot" style="left:221px;top:120px"></div>
  <div class="icon-dot" style="left:221px;top:164px"></div>
  <div class="icon-dot" style="left:221px;top:208px"></div>
  <div class="abs" style="left:292px;top:68px;width:232px">
    <div class="mini-head mini-head--blue">Heading goes here</div>
    <p class="body-tiny" style="margin-bottom:9px">Lorem Ipsum is simply dummy text of the printing and typesetting industry. Lorem Ipsum has been the industry's standard dummy text ever since the 1500s.</p>
    <div class="mini-head mini-head--blue">Heading goes here</div>
    <p class="body-tiny" style="margin-bottom:9px">Lorem Ipsum is simply dummy text of the printing and typesetting industry. Lorem Ipsum has been the industry's standard dummy text ever since the 1500s.</p>
    <div class="mini-head mini-head--blue">Heading goes here</div>
    <p class="body-tiny" style="margin-bottom:9px">Lorem Ipsum is simply dummy text of the printing and typesetting industry. Lorem Ipsum has been the industry's standard dummy text ever since the 1500s.</p>
    <div class="mini-head mini-head--blue">Heading goes here</div>
    <p class="body-tiny">Lorem Ipsum is simply dummy text of the printing and typesetting industry. Lorem Ipsum has been the industry's standard dummy text ever since the 1500s.</p>
  </div>
  <div class="slide-footer"><span class="globe"></span><span class="url">www.harrowfieldengines.example</span><div class="socials"><span></span><span></span><span></span></div><div class="page-no">1</div></div>
</div>

<!-- Table of contents -->
<div class="slide col-left row-3">
  <div class="slide-rule"></div>
  <div class="slide-heading">Table of Contents</div>
  <div class="brand brand--sm slide-brand"><span class="l1">HARROWFIELD</span><span class="l2">ENGINES</span></div>
  <div class="toc-item" style="left:24px;top:70px"><div class="toc-num">01</div><div><div class="mini-head">Content here</div><p class="body-tiny">Lorem Ipsum is simply dummy text of the printing and typesetting industry. Lorem Ipsum has been the industry's standard dummy text ever.</p></div></div>
  <div class="toc-item" style="left:24px;top:140px"><div class="toc-num">02</div><div><div class="mini-head">Content here</div><p class="body-tiny">Lorem Ipsum is simply dummy text of the printing and typesetting industry. Lorem Ipsum has been the industry's standard dummy text ever.</p></div></div>
  <div class="toc-item" style="left:24px;top:210px"><div class="toc-num">03</div><div><div class="mini-head">Content here</div><p class="body-tiny">Lorem Ipsum is simply dummy text of the printing and typesetting industry. Lorem Ipsum has been the industry's standard dummy text ever.</p></div></div>
  <div class="toc-item" style="left:290px;top:70px"><div class="toc-num">04</div><div><div class="mini-head">Content here</div><p class="body-tiny">Lorem Ipsum is simply dummy text of the printing and typesetting industry. Lorem Ipsum has been the industry's standard dummy text ever.</p></div></div>
  <div class="toc-item" style="left:290px;top:140px"><div class="toc-num">05</div><div><div class="mini-head">Content here</div><p class="body-tiny">Lorem Ipsum is simply dummy text of the printing and typesetting industry. Lorem Ipsum has been the industry's standard dummy text ever.</p></div></div>
  <div class="toc-item" style="left:290px;top:210px"><div class="toc-num">06</div><div><div class="mini-head">Content here</div><p class="body-tiny">Lorem Ipsum is simply dummy text of the printing and typesetting industry. Lorem Ipsum has been the industry's standard dummy text ever.</p></div></div>
  <div class="slide-footer"><span class="globe"></span><span class="url">www.harrowfieldengines.example</span><div class="socials"><span></span><span></span><span></span></div><div class="page-no">2</div></div>
</div>

<!-- Section title -->
<div class="slide col-right row-3">
  <div class="photo photo--mono" style="left:0;top:0;width:546px;height:306px" role="img" aria-label="Black and white curved glass building"></div>
  <div class="abs" style="left:0;top:118px;width:370px;height:86px;background:var(--blue)">
    <div class="title abs" style="left:28px;top:22px;font-size:26px;font-weight:700">SECTION TITLE</div>
    <div class="subtitle abs" style="left:28px;top:56px">Subtitle goes here</div>
  </div>
  <div class="abs" style="left:370px;top:118px;width:176px;height:86px;background:var(--navy)">
    <div class="brand brand--light brand--sm abs" style="left:0;width:176px;top:34px;transform:scale(1.35)"><span class="l1">HARROWFIELD</span><span class="l2">ENGINES</span></div>
  </div>
</div>

<!-- Biographies -->
<div class="slide col-left row-4">
  <div class="slide-rule"></div>
  <div class="slide-heading">Heading For Biographies</div>
  <div class="brand brand--sm slide-brand"><span class="l1">HARROWFIELD</span><span class="l2">ENGINES</span></div>
  <div class="photo photo--office" style="left:18px;top:72px;width:162px;height:68px" role="img" aria-label="Business handshake across a desk"></div>
  <div class="photo photo--office" style="left:190px;top:72px;width:162px;height:68px" role="img" aria-label="Team meeting around a table"></div>
  <div class="photo photo--mono" style="left:362px;top:72px;width:162px;height:68px" role="img" aria-label="Office tower seen from below"></div>
  <div class="bio-caption" style="left:18px;top:140px;width:162px">Who we are</div>
  <div class="bio-caption" style="left:190px;top:140px;width:162px">Our mission</div>
  <div class="bio-caption" style="left:362px;top:140px;width:162px">Our values</div>
  <div class="abs" style="left:18px;top:153px;width:162px;height:90px;background:#f3f4f6"><p class="body-tiny" style="padding:10px 8px;text-align:center">Lorem Ipsum is simply dummy text of the printing and typesetting industry. Lorem Ipsum has been the industry's standard dummy text ever since the 1500s, when an unknown printer took a galley of type and scrambled it.</p></div>
  <div class="abs" style="left:190px;top:153px;width:162px;height:90px;background:#f3f4f6"><p class="body-tiny" style="padding:10px 8px;text-align:center">Lorem Ipsum is simply dummy text of the printing and typesetting industry. Lorem Ipsum has been the industry's standard dummy text ever since the 1500s, when an unknown printer took a galley of type and scrambled it.</p></div>
  <div class="abs" style="left:362px;top:153px;width:162px;height:90px;background:#f3f4f6"><p class="body-tiny" style="padding:10px 8px;text-align:center">Lorem Ipsum is simply dummy text of the printing and typesetting industry. Lorem Ipsum has been the industry's standard dummy text ever since the 1500s, when an unknown printer took a galley of type and scrambled it.</p></div>
  <div class="slide-footer"><span class="globe"></span><span class="url">www.harrowfieldengines.example</span><div class="socials"><span></span><span></span><span></span></div><div class="page-no">4</div></div>
</div>

<!-- Pie charts -->
<div class="slide col-right row-4">
  <div class="slide-rule"></div>
  <div class="slide-heading">Pie Chart Goes Here</div>
  <div class="brand brand--sm slide-brand"><span class="l1">HARROWFIELD</span><span class="l2">ENGINES</span></div>
  <p class="body-tiny abs" style="left:100px;top:66px;width:346px;text-align:center">Lorem Ipsum is simply dummy text of the printing and typesetting industry. Lorem Ipsum has been the industry's standard dummy text ever since the 1500s.</p>
  <svg class="abs" style="left:0;top:100px" width="546" height="100" viewBox="0 0 546 100" aria-label="Three donut charts: 75, 65 and 50 percent">
    <g font-family="Montserrat, sans-serif" font-weight="600" font-size="13" fill="#7b8088" text-anchor="middle">
      <circle cx="108" cy="44" r="34" fill="none" stroke="var(--track)" stroke-width="12"/>
      <circle cx="108" cy="44" r="34" fill="none" stroke="var(--navy)" stroke-width="12" stroke-dasharray="160.2 213.6" transform="rotate(-90 108 44)"/>
      <text x="108" y="49" font-style="italic">75%</text>
      <circle cx="273" cy="44" r="34" fill="none" stroke="var(--track)" stroke-width="12"/>
      <circle cx="273" cy="44" r="34" fill="none" stroke="var(--blue)" stroke-width="12" stroke-dasharray="138.8 213.6" transform="rotate(-90 273 44)"/>
      <text x="273" y="49" font-style="italic">65%</text>
      <circle cx="438" cy="44" r="34" fill="none" stroke="var(--track)" stroke-width="12"/>
      <circle cx="438" cy="44" r="34" fill="none" stroke="var(--navy)" stroke-width="12" stroke-dasharray="106.8 213.6" transform="rotate(-90 438 44)"/>
      <text x="438" y="49" font-style="italic">50%</text>
    </g>
  </svg>
  <div class="abs" style="left:38px;top:206px;width:140px;text-align:center"><div class="mini-head">Content heading</div><p class="body-tiny">Lorem Ipsum is simply dummy text of the printing and typesetting industry. Lorem Ipsum has been the industry's standard dummy text ever</p></div>
  <div class="abs" style="left:203px;top:206px;width:140px;text-align:center"><div class="mini-head">Content heading</div><p class="body-tiny">Lorem Ipsum is simply dummy text of the printing and typesetting industry. Lorem Ipsum has been the industry's standard dummy text ever</p></div>
  <div class="abs" style="left:368px;top:206px;width:140px;text-align:center"><div class="mini-head">Content heading</div><p class="body-tiny">Lorem Ipsum is simply dummy text of the printing and typesetting industry. Lorem Ipsum has been the industry's standard dummy text ever</p></div>
  <div class="slide-footer"><span class="globe"></span><span class="url">www.harrowfieldengines.example</span><div class="socials"><span></span><span></span><span></span></div><div class="page-no">5</div></div>
</div>

<!-- Bar graph -->
<div class="slide col-left row-5">
  <div class="slide-rule"></div>
  <div class="slide-heading">Bar Graph Goes Here</div>
  <div class="brand brand--sm slide-brand"><span class="l1">HARROWFIELD</span><span class="l2">ENGINES</span></div>
  <svg class="abs" style="left:0;top:64px" width="546" height="210" viewBox="0 0 546 210" aria-label="Stacked monthly bar chart of receipts, sales and orders">
    <g font-family="Open Sans, sans-serif" font-size="4.5" fill="#7b8088">
      <circle cx="400" cy="8" r="2.5" fill="var(--track)"/><text x="405" y="10">Receipts</text>
      <circle cx="432" cy="8" r="2.5" fill="var(--blue)"/><text x="437" y="10">Sales</text>
      <circle cx="462" cy="8" r="2.5" fill="var(--navy)"/><text x="467" y="10">Orders</text>
      <g stroke="#e6e8eb" stroke-width=".6">
        <line x1="40" y1="24" x2="528" y2="24"/><line x1="40" y1="40" x2="528" y2="40"/><line x1="40" y1="56" x2="528" y2="56"/>
        <line x1="40" y1="72" x2="528" y2="72"/><line x1="40" y1="88" x2="528" y2="88"/><line x1="40" y1="104" x2="528" y2="104"/>
        <line x1="40" y1="120" x2="528" y2="120"/><line x1="40" y1="136" x2="528" y2="136"/><line x1="40" y1="152" x2="528" y2="152"/>
        <line x1="40" y1="168" x2="528" y2="168"/><line x1="40" y1="184" x2="528" y2="184"/>
      </g>
      <g text-anchor="end">
        <text x="36" y="26">100</text><text x="36" y="42">90</text><text x="36" y="58">80</text><text x="36" y="74">70</text>
        <text x="36" y="90">60</text><text x="36" y="106">50</text><text x="36" y="122">40</text><text x="36" y="138">30</text>
        <text x="36" y="154">20</text><text x="36" y="170">10</text><text x="36" y="186">0</text>
      </g>
      <!-- scale: 1.6 px per unit, baseline 184 -->
      <g>
        <rect x="52" y="171.2" width="22" height="12.8" fill="var(--track)"/><rect x="52" y="155.2" width="22" height="16" fill="var(--navy)"/><rect x="52" y="142.4" width="22" height="12.8" fill="var(--blue)"/>
        <rect x="92" y="152" width="22" height="32" fill="var(--track)"/><rect x="92" y="104" width="22" height="48" fill="var(--navy)"/><rect x="92" y="40" width="22" height="64" fill="var(--blue)"/>
        <rect x="132" y="168" width="22" height="16" fill="var(--track)"/><rect x="132" y="144" width="22" height="24" fill="var(--navy)"/><rect x="132" y="88" width="22" height="56" fill="var(--blue)"/>
        <rect x="172" y="160" width="22" height="24" fill="var(--track)"/><rect x="172" y="24" width="22" height="136" fill="var(--navy)"/>
        <rect x="212" y="120" width="22" height="64" fill="var(--track)"/><rect x="212" y="56" width="22" height="64" fill="var(--blue)"/>
        <rect x="252" y="164.8" width="22" height="19.2" fill="var(--track)"/><rect x="252" y="142.4" width="22" height="22.4" fill="var(--navy)"/>
        <rect x="292" y="144" width="22" height="40" fill="var(--track)"/><rect x="292" y="96" width="22" height="48" fill="var(--navy)"/><rect x="292" y="56" width="22" height="40" fill="var(--blue)"/>
        <rect x="332" y="152" width="22" height="32" fill="var(--track)"/><rect x="332" y="40" width="22" height="112" fill="var(--navy)"/>
        <rect x="372" y="164.8" width="22" height="19.2" fill="var(--track)"/><rect x="372" y="104" width="22" height="60.8" fill="var(--blue)"/>
        <rect x="412" y="128" width="22" height="56" fill="var(--track)"/><rect x="412" y="72" width="22" height="56" fill="var(--navy)"/>
        <rect x="452" y="152" width="22" height="32" fill="var(--track)"/><rect x="452" y="56" width="22" height="96" fill="var(--blue)"/>
        <rect x="492" y="171.2" width="22" height="12.8" fill="var(--track)"/><rect x="492" y="126.4" width="22" height="44.8" fill="var(--navy)"/>
      </g>
      <g text-anchor="middle">
        <text x="63" y="194">JAN</text><text x="103" y="194">FEB</text><text x="143" y="194">MAR</text><text x="183" y="194">APR</text>
        <text x="223" y="194">MAY</text><text x="263" y="194">JUN</text><text x="303" y="194">JUL</text><text x="343" y="194">AUG</text>
        <text x="383" y="194">SEP</text><text x="423" y="194">OCT</text><text x="463" y="194">NOV</text><text x="503" y="194">DEC</text>
      </g>
    </g>
  </svg>
  <div class="slide-footer"><span class="globe"></span><span class="url">www.harrowfieldengines.example</span><div class="socials"><span></span><span></span><span></span></div><div class="page-no">6</div></div>
</div>

<!-- Features with photo -->
<div class="slide col-right row-5">
  <div class="slide-rule"></div>
  <div class="slide-heading">Headline Goes Here</div>
  <div class="brand brand--sm slide-brand" style="right:22px"><span class="l1">HARROWFIELD</span><span class="l2">ENGINES</span></div>
  <div class="photo photo--glass" style="left:340px;top:62px;width:206px;height:196px" role="img" aria-label="Reflective glass building against a cloudy sky"></div>
  <div class="feature" style="left:12px;top:68px"><div class="ring"></div><div class="mini-head" style="font-size:5px">Heading goes here</div><p class="body-micro">Lorem Ipsum is simply dummy text of the printing and typesetting industry. Lorem Ipsum has been the industry's standard dummy text ever since the 1500s.</p></div>
  <div class="feature" style="left:117px;top:68px"><div class="ring"></div><div class="mini-head" style="font-size:5px">Heading goes here</div><p class="body-micro">Lorem Ipsum is simply dummy text of the printing and typesetting industry. Lorem Ipsum has been the industry's standard dummy text ever since the 1500s.</p></div>
  <div class="feature" style="left:222px;top:68px"><div class="ring"></div><div class="mini-head" style="font-size:5px">Heading goes here</div><p class="body-micro">Lorem Ipsum is simply dummy text of the printing and typesetting industry. Lorem Ipsum has been the industry's standard dummy text ever since the 1500s.</p></div>
  <div class="feature" style="left:12px;top:172px"><div class="ring"></div><div class="mini-head" style="font-size:5px">Heading goes here</div><p class="body-micro">Lorem Ipsum is simply dummy text of the printing and typesetting industry. Lorem Ipsum has been the industry's standard dummy text ever since the 1500s.</p></div>
  <div class="feature" style="left:117px;top:172px"><div class="ring"></div><div class="mini-head" style="font-size:5px">Heading goes here</div><p class="body-micro">Lorem Ipsum is simply dummy text of the printing and typesetting industry. Lorem Ipsum has been the industry's standard dummy text ever since the 1500s.</p></div>
  <div class="feature" style="left:222px;top:172px"><div class="ring"></div><div class="mini-head" style="font-size:5px">Heading goes here</div><p class="body-micro">Lorem Ipsum is simply dummy text of the printing and typesetting industry. Lorem Ipsum has been the industry's standard dummy text ever since the 1500s.</p></div>
  <div class="slide-footer"><span class="globe"></span><span class="url">www.harrowfieldengines.example</span><div class="socials"><span></span><span></span><span></span></div><div class="page-no">7</div></div>
</div>

<!-- Cycle diagram -->
<div class="slide col-left row-6">
  <div class="slide-rule"></div>
  <div class="slide-heading">Headline Goes Here</div>
  <div class="brand brand--sm slide-brand"><span class="l1">HARROWFIELD</span><span class="l2">ENGINES</span></div>
  <svg class="abs" style="left:193px;top:58px" width="160" height="160" viewBox="-80 -80 160 160" aria-label="Six-part cycle diagram">
    <g fill="none" stroke-width="34">
      <circle r="52" stroke="var(--navy)" stroke-dasharray="52.5 274.2" transform="rotate(-90)"/>
      <circle r="52" stroke="#2f8fd8" stroke-dasharray="52.5 274.2" transform="rotate(-30)"/>
      <circle r="52" stroke="var(--blue)" stroke-dasharray="52.5 274.2" transform="rotate(30)"/>
      <circle r="52" stroke="#2f8fd8" stroke-dasharray="52.5 274.2" transform="rotate(90)"/>
      <circle r="52" stroke="var(--navy)" stroke-dasharray="52.5 274.2" transform="rotate(150)"/>
      <circle r="52" stroke="var(--navy-deep)" stroke-dasharray="52.5 274.2" transform="rotate(210)"/>
    </g>
    <circle r="33" fill="#fff" stroke="#dbe7f6" stroke-width="3"/>
    <g fill="#fff">
      <circle cx="26" cy="-45" r="5"/><circle cx="52" cy="0" r="5"/><circle cx="26" cy="45" r="5"/>
      <circle cx="-26" cy="45" r="5"/><circle cx="-52" cy="0" r="5"/><circle cx="-26" cy="-45" r="5"/>
    </g>
    <text y="-1" text-anchor="middle" font-family="Montserrat, sans-serif" font-weight="700" font-size="8" fill="var(--navy)">HARROWFIELD</text>
    <text y="8" text-anchor="middle" font-family="Montserrat, sans-serif" font-weight="700" font-size="4.5" letter-spacing="2" fill="var(--navy)">ENGINES</text>
  </svg>
  <div class="abs" style="left:20px;top:70px;width:170px;text-align:right"><div class="mini-head">Headline goes here</div><p class="body-micro">Lorem Ipsum is simply dummy text of the printing and typesetting industry. Lorem Ipsum has been the industry's standard dummy text ever since the 1500s, when an unknown printer took a galley of type.</p></div>
  <div class="abs" style="left:8px;top:138px;width:170px;text-align:right"><div class="mini-head">Headline goes here</div><p class="body-micro">Lorem Ipsum is simply dummy text of the printing and typesetting industry. Lorem Ipsum has been the industry's standard dummy text ever since the 1500s, when an unknown printer took a galley of type.</p></div>
  <div class="abs" style="left:20px;top:206px;width:170px;text-align:right"><div class="mini-head">Headline goes here</div><p class="body-micro">Lorem Ipsum is simply dummy text of the printing and typesetting industry. Lorem Ipsum has been the industry's standard dummy text ever since the 1500s, when an unknown printer took a galley of type.</p></div>
  <div class="abs" style="left:358px;top:70px;width:170px"><div class="mini-head">Headline goes here</div><p class="body-micro">Lorem Ipsum is simply dummy text of the printing and typesetting industry. Lorem Ipsum has been the industry's standard dummy text ever since the 1500s, when an unknown printer took a galley of type.</p></div>
  <div class="abs" style="left:370px;top:138px;width:170px"><div class="mini-head">Headline goes here</div><p class="body-micro">Lorem Ipsum is simply dummy text of the printing and typesetting industry. Lorem Ipsum has been the industry's standard dummy text ever since the 1500s, when an unknown printer took a galley of type.</p></div>
  <div class="abs" style="left:358px;top:206px;width:170px"><div class="mini-head">Headline goes here</div><p class="body-micro">Lorem Ipsum is simply dummy text of the printing and typesetting industry. Lorem Ipsum has been the industry's standard dummy text ever since the 1500s, when an unknown printer took a galley of type.</p></div>
  <div class="slide-footer"><span class="globe"></span><span class="url">www.harrowfieldengines.example</span><div class="socials"><span></span><span></span><span></span></div><div class="page-no">8</div></div>
</div>

<!-- Contact -->
<div class="slide col-right row-6">
  <div class="network-fill" style="left:0;top:0;width:546px;height:138px" role="img" aria-label="Faint hexagonal network pattern"></div>
  <div class="brand brand--lg abs" style="left:0;width:546px;top:62px"><span class="l1">HARROWFIELD</span><span class="l2">ENGINES</span></div>
  <div class="band" style="top:138px;height:123px">
    <div class="title abs" style="left:0;width:546px;text-align:center;top:14px;font-size:23px">Contact us</div>
    <p class="abs" style="left:0;width:546px;text-align:center;top:48px;font-size:9px;line-height:1.4;color:#fff">Location: 45 Larkspur Lane, Eastmoor 4021<br>Email Address : hello@harrowfieldengines.example<br>Phone Number: (555) 0142-7730</p>
    <div class="socials abs" style="left:255px;top:100px"><span></span><span></span><span></span></div>
  </div>
  <div class="url abs" style="left:0;width:546px;text-align:center;top:278px">www.harrowfieldengines.example</div>
</div>

<div class="brand watermark"><span class="l1">HARROWFIELD</span><span class="l2">ENGINES</span></div>

</body>
</html>
```